Elmrow Management real estate management company needs presentation folder to hand clients

looking for a folder with pockets that represent my real estate management company when i hand to client reports or promotional material. I only do resedential real estate. I want classy and professional - pictures or additioal graphixs are fine

when a client open i will usally insert text and reports about my business
also on the inside flap is usally place for my business card i will upload a picture so the theme can be constant

Target Market(s)

my existing real estate cleints
and i will use when i am soliciting new business

Industry/Entity Type

Real Estate

Font styles to use
Serif

Requirements
Must have
• must have logo
• must give appearance of professionalism and maturity
• have basic company info tel# ,address
• id like viewer to know I manage real estate - focus on residential small to large apartment buildings
• not strip malls, not giganic complexes - im a mid size company
• logo is black but i welcome color as u see fit
Nice to have
• maybe pictures
• my slogan - " we will manage your building like its our own "
• focus on professioanl, safe, trust worthy
• type style should be clear and readable - but im open to sugestions

```html
<!DOCTYPE html>
<html lang="en">
<head>
<meta charset="utf-8">
<title>Elmrow Management – Presentation Folder</title>
<link rel="stylesheet" href="https://fonts.googleapis.com/css2?family=Montserrat:wght@300;400;600;700&display=swap">
<style>
  :root{
    --board:#b4aba5;
    --paper:#ffffff;
    --paper-warm:#f2f0ee;
    --ink:#111111;
    --ink-soft:#444444;
    --sky-top:#b9b6d3;
    --sky-pink:#e3c3cf;
    --house:#7f8cab;
    --roof:#2e344d;
    --ground:#5d6479;
  }
  *{box-sizing:border-box;margin:0;padding:0}
  html,body{width:680px;height:1200px;overflow:hidden}
  body{background:var(--board);font-family:"Montserrat",sans-serif;color:var(--ink);position:relative}
  .abs{position:absolute}
  .sheet{background:var(--paper);box-shadow:0 2px 6px rgba(0,0,0,.25)}

  /* brand name mark */
  .brand{display:flex;align-items:center;gap:4px;font-weight:700;letter-spacing:.08em;text-transform:uppercase;white-space:nowrap}
  .brand-square{width:7px;height:7px;background:currentColor;flex:none}
  .brand-name{font-size:6px}

  /* cover spread */
  .cover{left:78px;top:100px;width:554px;height:370px}
  .cover-panel{top:0;height:370px;width:275px}
  .cover-panel--back{left:0}
  .cover-panel--front{left:279px}
  .cover-photo{position:absolute;left:0;top:0}
  .cover-fold{left:275px;top:0;width:4px;height:370px;background:var(--board)}
  .cover-contact{left:0;width:275px;top:316px;text-align:center}
  .name{font-weight:700;letter-spacing:.02em}
  .title{font-weight:400;text-transform:uppercase;letter-spacing:.04em}
  .cover-contact .name{font-size:7px}
  .cover-contact .title{font-size:3.5px}
  .cover-contact .address{font-size:5px;margin-top:3px}
  .cover-contact .getintouch{font-size:4.5px;margin-top:8px}
  .cover-contact .getintouch b{font-weight:700}
  .cover-brand-back{left:134px;top:35px}
  .cover-brand-back .brand{flex-direction:column;gap:2px}
  .cover-brand-back .brand-name{font-size:4.5px}
  .cover-id{right:18px;top:26px;text-align:right}
  .cover-id .brand{justify-content:flex-end;margin-bottom:6px}
  .cover-id .name{font-size:12px;line-height:1}
  .cover-id .title{font-size:6px}
  .slogan{text-transform:uppercase;font-weight:300;line-height:1.05}
  .slogan b{font-weight:700}
  .cover-slogan{left:302px;top:306px;font-size:12px}

  /* business cards */
  .card{top:538px;width:188px;height:112px}
  .card--front{left:140px;background:var(--paper)}
  .card--back{left:340px;background:var(--ink);color:var(--paper)}
  .card-name{left:16px;top:34px}
  .card-name .name{font-size:9px;line-height:1}
  .card-name .title{font-size:4.5px}
  .card-brand{right:16px;top:24px}
  .card-brand .brand-name{font-size:5px}
  .card-details{left:16px;top:66px;font-size:5.2px;line-height:1.2}
  .card-details b{font-weight:700}
  .card-slogan{right:16px;top:84px;font-size:5.6px;text-align:right}
  .card--back .card-brand{left:16px;right:auto;top:22px}
  .card-slogan--back{left:16px;top:70px;font-size:11.5px;color:var(--paper)}

  /* inside spread */
  .inside{left:65px;top:712px;width:549px;height:366px}
  .inside-panel{top:0;height:366px}
  .inside-panel--left{left:0;width:275px;background:var(--paper)}
  .inside-panel--right{left:277px;width:272px;background:var(--paper-warm)}
  .letter{width:230px;background:var(--paper);box-shadow:0 1px 4px rgba(0,0,0,.25);overflow:hidden}
  .letter--left{left:16px;top:32px;height:220px}
  .letter--right{left:308px;top:32px;height:220px}
  .letter-band{height:18px;margin-top:14px;background:var(--ink);color:var(--paper);display:flex;align-items:center;justify-content:space-between;padding:0 8px}
  .letter-band .brand-name{font-size:3.5px}
  .letter-band .band-slogan{font-size:4.2px;font-weight:600}
  .letter-title{font-size:5px;font-weight:700;letter-spacing:.12em;text-align:center;margin-top:18px}
  .letter-ref{font-size:3.2px;text-align:center}
  .letter-body{padding:0 22px;font-size:3.3px;line-height:1.35}
  .letter-body .to{margin-top:16px}
  .letter-body .to b{font-weight:700;display:block}
  .letter-body .re{font-weight:700;font-style:normal;margin-top:10px}
  .letter-body p{margin-top:6px}
  .letter--right .letter-title{text-align:left;padding-left:15px;margin-top:18px}
  .letter--right .to{padding-left:15px;font-size:3.3px;line-height:1.35;margin-top:12px}
  .letter--right .to b{font-weight:700;display:block}
  .letter-photo{left:4px;top:76px;width:226px;height:94px;background:linear-gradient(180deg,#3a3f55 0%,#8d7584 28%,#5a5560 45%,#2c2a30 75%,#4a4b55 100%)}

  .pocket{top:236px;height:130px}
  .pocket--left{left:0;width:275px}
  .pocket--right{left:277px;width:272px}
  .pocket svg{position:absolute;left:0;top:0}
  .pocket-card{left:88px;top:268px;width:110px;height:62px;background:var(--paper);border-radius:9px;box-shadow:0 1px 3px rgba(0,0,0,.3)}
  .pocket-card .card-name{left:10px;top:20px}
  .pocket-card .name{font-size:5.4px;line-height:1}
  .pocket-card .title{font-size:2.6px}
  .pocket-card .card-brand{right:9px;top:14px}
  .pocket-card .brand-name{font-size:3px}
  .pocket-card .brand-square{width:4px;height:4px}
  .pocket-card .card-details{left:10px;top:38px;font-size:3px}
  .pocket-card .card-slogan{right:9px;top:48px;font-size:3.2px}
  .pocket-slogan{right:20px;top:264px;text-align:right;font-size:7.5px}
  .pocket-brand{right:20px;top:250px}
  .pocket-brand .brand-name{font-size:3.5px}
  .pocket-brand .brand-square{width:4px;height:4px}

  /* closing mark */
  .closing{left:0;width:680px;top:1112px;display:flex;flex-direction:column;align-items:center;gap:12px}
  .closing .brand-name{font-size:9px}
  .closing .brand-square{width:10px;height:10px}
  .closing .name{font-size:18px}
</style>
</head>
<body>

<!-- Folder outside -->
<section class="abs cover">
  <div class="abs sheet cover-panel cover-panel--back"></div>
  <div class="abs sheet cover-panel cover-panel--front"></div>
  <svg class="cover-photo" width="554" height="370" viewBox="0 0 554 370" role="img" aria-label="Photograph of a two-storey suburban house with garage at dusk">
    <defs>
      <linearGradient id="dusk" x1="0" y1="0" x2="0" y2="1">
        <stop offset="0" stop-color="var(--sky-top)"/>
        <stop offset=".25" stop-color="var(--sky-pink)"/>
        <stop offset=".45" stop-color="var(--roof)"/>
        <stop offset=".65" stop-color="var(--house)"/>
        <stop offset="1" stop-color="var(--ground)"/>
      </linearGradient>
    </defs>
    <polygon points="0,102 276,54 554,130 554,298 278,370 0,298" fill="url(#dusk)"/>
  </svg>
  <div class="abs cover-fold"></div>

  <div class="abs cover-brand-back">
    <div class="brand"><span class="brand-square"></span><span class="brand-name">Elmrow Management</span></div>
  </div>
  <div class="abs cover-contact">
    <div class="name">DANIEL MARSH</div>
    <div class="title">Master Building Manager</div>
    <div class="address">24 Alder Court Suite 210 Westbrook, NY 10620</div>
    <div class="getintouch"><b>Get in touch</b> &nbsp;|&nbsp; ☐ 914 555 0142 &nbsp; ✆ 917 555 0187 &nbsp; ✉ office@elmrowmgmt.com</div>
  </div>

  <div class="abs cover-id">
    <div class="brand"><span class="brand-square"></span><span class="brand-name">Elmrow Management</span></div>
    <div class="name">DANIEL MARSH</div>
    <div class="title">Master Building Manager</div>
  </div>
  <div class="abs slogan cover-slogan">We will<br>manage your building<br><b>like it is our own</b></div>
</section>

<!-- Business cards -->
<section class="abs sheet card card--front">
  <div class="abs card-name"><div class="name">DANIEL MARSH</div><div class="title">Master Building Manager</div></div>
  <div class="abs card-brand"><div class="brand"><span class="brand-square"></span><span class="brand-name">Elmrow Management</span></div></div>
  <div class="abs card-details">24 Alder Court Suite 210<br>Westbrook, NY 10620<br><b>M</b> / 914 555 0142<br><b>P</b> / 917 555 0187<br><b>E</b> / office@elmrowmgmt.com</div>
  <div class="abs slogan card-slogan">We will<br>manage your building<br><b>like it is our own</b></div>
</section>
<section class="abs sheet card card--back">
  <div class="abs card-brand"><div class="brand"><span class="brand-square"></span><span class="brand-name">Elmrow Management</span></div></div>
  <div class="abs slogan card-slogan--back">We will<br>manage your building<br><b>like it is our own</b></div>
</section>

<!-- Folder inside -->
<section class="abs inside">
  <div class="abs sheet inside-panel inside-panel--left"></div>
  <div class="abs sheet inside-panel inside-panel--right"></div>

  <article class="abs letter letter--left">
    <div class="letter-band">
      <div class="brand"><span class="brand-square"></span><span class="brand-name">Elmrow Management</span></div>
      <span class="band-slogan">We Will Manage Your Building Like It Is Our Own</span>
    </div>
    <div class="letter-title">PROPERTY OFFER</div>
    <div class="letter-ref">#175280</div>
    <div class="letter-body">
      <div class="to"><b>Mei Tran</b>Parkside Residences<br>12 Cedar Lane<br>Belmont 3216</div>
      <div class="re">Re : Routine Service of Fire Protection System and Equipment Proposal</div>
      <p>Dear Mei,</p>
      <p>Thank you for considering our team for the care of your residential property. We offer routine inspection of fire protection systems, tenant-friendly scheduling and clear monthly reporting. Every visit is logged and shared with you within two business days.</p>
      <p>Our proposal covers alarms, extinguishers, sprinklers and emergency lighting across all floors. Pricing is fixed for twelve months and includes after-hours response. Please review the attached schedule and contact our office with any questions before signing.</p>
    </div>
  </article>

  <article class="abs letter letter--right">
    <div class="letter-title">PROPERTY OFFER</div>
    <div class="to"><b>Mei Tran</b>Parkside Residences<br>12 Cedar Lane<br>Belmont 3216</div>
    <div class="abs letter-photo" role="img" aria-label="Photograph of a row of modern townhouses at dusk"></div>
  </article>

  <div class="abs pocket pocket--left">
    <svg width="275" height="130" viewBox="0 0 275 130">
      <polygon points="0,0 262,0 275,14 275,130 0,130" fill="var(--paper)" stroke="#dddddd" stroke-width=".5"/>
    </svg>
  </div>
  <div class="abs pocket pocket--right">
    <svg width="272" height="130" viewBox="0 0 272 130" role="img" aria-label="Photograph of a suburban house at dusk on the pocket">
      <defs>
        <linearGradient id="pocketDusk" x1="0" y1="0" x2="0" y2="1">
          <stop offset="0" stop-color="var(--sky-top)"/>
          <stop offset=".4" stop-color="var(--sky-pink)"/>
          <stop offset=".7" stop-color="var(--house)"/>
          <stop offset="1" stop-color="var(--roof)"/>
        </linearGradient>
      </defs>
      <polygon points="6,0 272,0 272,130 0,130 0,8" fill="url(#pocketDusk)"/>
    </svg>
  </div>
  <div class="abs pocket-card">
    <div class="abs card-name"><div class="name">DANIEL MARSH</div><div class="title">Master Building Manager</div></div>
    <div class="abs card-brand"><div class="brand"><span class="brand-square"></span><span class="brand-name">Elmrow Mgmt</span></div></div>
    <div class="abs card-details">24 Alder Court Suite 210<br>Westbrook, NY 10620<br>M / 914 555 0142</div>
    <div class="abs slogan card-slogan">We will<br><b>like it is our own</b></div>
  </div>
  <div class="abs pocket-brand"><div class="brand"><span class="brand-square"></span><span class="brand-name">Elmrow Management</span></div></div>
  <div class="abs slogan pocket-slogan">We will<br>manage your building<br><b>like it is our own</b></div>
</section>

<!-- Closing mark -->
<footer class="abs closing">
  <div class="brand"><span class="brand-square"></span><span class="brand-name">Elmrow Management</span></div>
  <div class="name">DANIEL MARSH</div>
</footer>

</body>
</html>
```